TIDAL VERGE needs bisness cards pronto

Bisness name is "TIDAL VERGE" new bisness the bisness includes lawn mowing, garden matanace, and any jobs around the house.
I need a card that is colorful and vibrant and the bisness of lawn mowing maybe with some nature with it. It also needs my contact details"Darren Quellby mobile 0413562049 call for free quote and email norma.vance@fernmail.com.au and a catchy tag line

Industry/Entity Type

House

Requirements
Must have
• Bisness name "TIDAL VERGE"
Contact details "0413562049"
Email norma.vance@fernmail.com.au
Call for free quote

```html
<!DOCTYPE html>
<html lang="en">
<head>
<meta charset="utf-8">
<title>TIDAL VERGE — Business Cards</title>
<link rel="stylesheet" href="https://fonts.googleapis.com/css2?family=Open+Sans:wght@600;700;800&display=swap">
<style>
  :root {
    --page-bg: #e8e3d9;
    --card-green: #2e4a39;
    --card-edge: #223829;
    --white: #ffffff;
    --tag-salmon: #e4805f;
    --tag-lime: #8cc152;
    --tag-red: #e0312f;
    --chip-slate: #34495b;
    --chip-cream: #f4f0cc;
    --ink: #1b2a22;
    --band-black: #0b0d0b;
  }
  * { box-sizing: border-box; margin: 0; padding: 0; }
  html, body {
    width: 937px;
    height: 1200px;
    overflow: hidden;
  }
  body {
    background: var(--page-bg);
    font-family: "Open Sans", Arial, sans-serif;
    position: relative;
  }
  .card {
    position: absolute;
    left: 88px;
    width: 760px;
    height: 440px;
    background: var(--card-green);
    box-shadow: 0 6px 0 var(--card-edge), 0 14px 30px rgba(0,0,0,0.25);
    overflow: hidden;
  }
  .card--back { top: 110px; }
  .card--front { top: 640px; }

  .wordmark {
    position: absolute;
    color: var(--white);
    font-weight: 800;
    line-height: 0.88;
    letter-spacing: 1px;
    text-transform: uppercase;
  }
  .card--back .wordmark {
    left: 50%;
    top: 50%;
    transform: translate(-50%, -50%);
    font-size: 120px;
  }
  .card--front .wordmark {
    left: 40px;
    top: 170px;
    font-size: 76px;
  }

  .service-tag {
    position: absolute;
    right: 0;
    color: var(--white);
    font-weight: 700;
    font-size: 24px;
    line-height: 1;
    padding: 6px 22px 6px 18px;
    text-align: right;
  }
  .service-tag--mowing { top: 34px; background: var(--tag-salmon); }
  .service-tag--garden { top: 74px; background: var(--tag-lime); }
  .service-tag--jobs {
    top: 114px;
    background: var(--tag-red);
    line-height: 1.05;
    padding: 7px 22px 7px 18px;
  }

  .contact {
    position: absolute;
    display: flex;
    align-items: center;
    gap: 10px;
    font-weight: 700;
    padding: 8px 16px;
  }
  .contact svg { flex: none; }
  .contact--phone {
    top: 200px;
    right: 40px;
    background: var(--chip-slate);
    color: var(--white);
    font-size: 26px;
  }
  .contact--email {
    top: 318px;
    left: 110px;
    background: var(--chip-cream);
    color: var(--ink);
    font-size: 21px;
  }
  .call-to-action {
    position: absolute;
    left: 130px;
    bottom: 0;
    width: 270px;
    height: 62px;
    background: var(--band-black);
    color: var(--white);
    font-weight: 700;
    font-size: 22px;
    display: flex;
    align-items: center;
    justify-content: center;
  }
</style>
</head>
<body>
  <section class="card card--back" aria-label="Business card, back">
    <h1 class="wordmark">Tidal<br>Verge</h1>
  </section>

  <section class="card card--front" aria-label="Business card, front">
    <div class="service-tag service-tag--mowing">lawn mowing</div>
    <div class="service-tag service-tag--garden">garden matanace</div>
    <div class="service-tag service-tag--jobs">any jobs around<br>the house</div>

    <div class="contact contact--phone">
      <svg width="26" height="22" viewBox="0 0 26 22" aria-hidden="true">
        <path d="M2 7 C2 2 24 2 24 7 L24 9 L18 9 L18 6 L8 6 L8 9 L2 9 Z" fill="#0e1a14"/>
        <path d="M6 10 L20 10 L23 20 L3 20 Z" fill="#0e1a14"/>
        <circle cx="13" cy="15" r="2.5" fill="#34495b"/>
      </svg>
      <span>0413562049</span>
    </div>

    <h2 class="wordmark">Tidal<br>Verge</h2>

    <div class="contact contact--email">
      <svg width="26" height="18" viewBox="0 0 26 18" aria-hidden="true">
        <rect x="0" y="0" width="26" height="18" fill="#1b2a22"/>
        <path d="M1 1 L13 10 L25 1" fill="none" stroke="#f4f0cc" stroke-width="1.6"/>
      </svg>
      <span>norma.vance@fernmail.com.au</span>
    </div>

    <div class="call-to-action">Call for free quote</div>
  </section>
</body>
</html>
```